Brightpath Letterhead

We would like a letterhead for our company. I have uploaded our logo.

Brightpath Ridge Consulting
1450 W Corliss Ave Ste 310
Arlington, TX 76006
833-517-2906

```html
<!DOCTYPE html>
<html lang="en">
<head>
<meta charset="utf-8">
<title>Brightpath Ridge Consulting – Letterhead</title>
<link rel="stylesheet" href="https://fonts.googleapis.com/css2?family=Josefin+Sans:wght@400;600&display=swap">
<style>
  :root {
    --brand-green: #6eff7a;
    --brand-teal: #136570;
    --soft-teal: #aecbcf;
    --soft-green: #d2fdd6;
    --paper: #fdfdfd;
  }
  * { margin: 0; padding: 0; box-sizing: border-box; }
  html, body {
    width: 848px;
    height: 1200px;
    overflow: hidden;
    background: var(--paper);
  }
  .letterhead {
    position: relative;
    width: 848px;
    height: 1200px;
    background: var(--paper);
    overflow: hidden;
    font-family: "Josefin Sans", sans-serif;
  }
  .top-band {
    position: absolute;
    top: 0; left: 0;
    width: 100%;
    height: 16px;
    display: flex;
  }
  .top-band__green { flex: 0 0 424px; background: var(--brand-green); }
  .top-band__teal { flex: 1; background: var(--brand-teal); }

  .brand {
    position: absolute;
    top: 44px;
    left: 42px;
    display: flex;
    align-items: center;
    gap: 14px;
  }
  .brand__dot {
    width: 44px;
    height: 44px;
    border-radius: 50%;
    background: var(--brand-teal);
  }
  .brand__name {
    font-weight: 600;
    font-size: 20px;
    letter-spacing: 0.13em;
    text-transform: uppercase;
    color: var(--brand-teal);
    line-height: 1;
    padding-top: 4px;
  }

  .contact {
    position: absolute;
    top: 48px;
    right: 40px;
    text-align: right;
    font-weight: 400;
    font-size: 11px;
    line-height: 1.45;
    letter-spacing: 0.04em;
    color: var(--brand-teal);
    font-style: normal;
  }

  .header-rule {
    position: absolute;
    top: 110px;
    left: 40px;
    width: 768px;
    height: 1.5px;
    background: var(--brand-green);
  }

  .corner-accent {
    position: absolute;
    left: 575px;
    top: 914px;
    width: 273px;
    height: 286px;
    border-top-left-radius: 100%;
    background:
      radial-gradient(circle at 30% 40%, var(--soft-teal) 0%, rgba(174,203,207,0) 65%),
      radial-gradient(circle at 80% 75%, var(--soft-green) 0%, rgba(210,253,214,0) 70%),
      linear-gradient(135deg, var(--soft-teal), var(--soft-green));
    opacity: 0.9;
  }
</style>
</head>
<body>
  <main class="letterhead">
    <div class="top-band">
      <div class="top-band__green"></div>
      <div class="top-band__teal"></div>
    </div>

    <header class="brand">
      <span class="brand__dot"></span>
      <span class="brand__name">Brightpath Ridge Consulting</span>
    </header>

    <address class="contact">
      1450 W Corliss Ave Ste 310<br>
      Arlington, TX 76006<br>
      833-517-2906
    </address>

    <div class="header-rule"></div>

    <div class="corner-accent" role="img" aria-label="Soft teal and green decorative brand shapes in the corner"></div>
  </main>
</body>
</html>
```